Tavrinel House

I am looking at a A4 one sided fact sheet about the property I developed, which I can print off or send electronically
Our current logo is Navy blue and Maroon colors
House

```html
<!DOCTYPE html>
<html lang="en">
<head>
<meta charset="utf-8">
<title>Tavrinel House – Property Fact Sheet</title>
<link rel="stylesheet" href="https://fonts.googleapis.com/css2?family=Anton&family=Lato:wght@400;700&display=swap">
<style>
  :root {
    --maroon: #7a1114;
    --navy: #1d3d86;
    --navy-deep: #15347a;
    --button-blue: #2a52ad;
    --ink: #3a3a3a;
    --logo-grey: #555555;
    --paper: #ffffff;
    --backdrop: #b3b3b3;
  }
  * { margin: 0; padding: 0; box-sizing: border-box; }
  html, body { width: 1200px; height: 1200px; overflow: hidden; }
  body { background: var(--backdrop); font-family: "Lato", sans-serif; }

  .sheet-frame {
    position: absolute; left: 208px; top: 49px;
    width: 785px; height: 1102px;
  }
  .sheet {
    position: absolute; left: 0; top: 0;
    width: 872px; height: 1224px;
    background: var(--paper);
    transform: scale(0.9); transform-origin: top left;
    box-shadow: 0 4px 14px rgba(0,0,0,0.3);
    overflow: hidden;
  }
  .abs { position: absolute; }

  .logo-text {
    left: 63px; top: 88px;
    font-family: "Anton", sans-serif; font-size: 66px; letter-spacing: 1px;
    color: var(--logo-grey); line-height: 1;
  }
  .maroon { background: var(--maroon); }

  .photo-building {
    left: 445px; top: 31px; width: 403px; height: 352px;
    background: linear-gradient(180deg, #8fb3e6 0%, #c3d1e6 25%, #8a6b5c 45%, #4d4a4c 75%, #2b2b2f 100%);
  }
  .photo-gym {
    left: 0; top: 235px; width: 598px; height: 290px;
    background: linear-gradient(180deg, #e8ecef 0%, #d7dbdc 35%, #a8a39f 60%, #6b6b6d 85%, #4c4c50 100%);
  }
  .photo-boardroom {
    left: 615px; top: 396px; width: 233px; height: 139px;
    background: linear-gradient(180deg, #b98a5e 0%, #e8e2d6 35%, #d5cfc3 60%, #6e7075 100%);
  }

  .facts { left: 0; top: 536px; width: 392px; }
  .fact {
    height: 83.5px; padding: 17px 0 0 46px;
    color: #fff; white-space: nowrap;
  }
  .fact-label { font-weight: 700; font-size: 19px; line-height: 22px; }
  .fact-value { font-size: 20px; line-height: 24px; margin-top: 6px; margin-left: -2px; }
  .fact-name .fact-label { font-weight: 400; font-size: 18px; }
  .fact-name .fact-value { font-weight: 700; font-size: 24px; line-height: 28px; margin-top: 1px; margin-left: 0; }
  .fact-small .fact-value { font-size: 18px; margin-top: 3px; }
  .fact:nth-child(1) { background: linear-gradient(180deg, #9fc0fa, #6f9bf0); }
  .fact:nth-child(2) { background: #5283e6; }
  .fact:nth-child(3) { background: #4776d8; }
  .fact:nth-child(4) { background: #3d69c8; }
  .fact:nth-child(5) { background: #335bb6; }
  .fact:nth-child(6) { background: #284ea0; }
  .fact:nth-child(7) { background: #1f428e; }
  .fact:nth-child(8) { background: var(--navy-deep); }

  .strategy { left: 421px; top: 584px; width: 414px; }
  .strategy-title {
    font-family: "Anton", sans-serif; font-size: 28px; color: var(--maroon);
    line-height: 1.15; margin-bottom: 4px; letter-spacing: 0.2px;
  }
  .strategy-body p {
    font-size: 16.6px; line-height: 20.5px; color: var(--ink);
    text-align: justify; letter-spacing: -0.1px;
  }
  .strategy-body p.gap { margin-top: 7px; }

  .cta-button {
    left: 421px; top: 994px; width: 356px; height: 46px;
    background: var(--button-blue); padding: 4px;
  }
  .cta-button span {
    display: flex; align-items: center; justify-content: center;
    height: 100%; border: 1.5px dashed #fff;
    color: #fff; font-weight: 700; font-size: 17px;
  }

  .call-title {
    left: 425px; top: 1056px;
    font-family: "Anton", sans-serif; font-size: 31px; color: var(--maroon); line-height: 1.1;
  }
  .call-phone {
    left: 425px; top: 1094px;
    font-weight: 700; font-size: 21px; color: #444;
  }
  .rule-navy { left: 551px; top: 1134px; width: 321px; height: 8px; background: var(--navy); }

  .web-band { left: 426px; top: 1150px; width: 446px; height: 52px; }
  .web-line {
    left: 474px; top: 1150px; height: 52px;
    display: flex; align-items: center; gap: 18px;
    color: #fff; font-weight: 700; font-size: 15px; letter-spacing: 4.6px;
  }
</style>
</head>
<body>
<div class="sheet-frame">
  <article class="sheet">
    <div class="abs logo-text">YOUR LOGO</div>

    <div class="abs maroon" style="left:432px; top:21px; width:403px; height:10px;"></div>
    <div class="abs maroon" style="left:432px; top:21px; width:13px; height:192px;"></div>
    <div class="abs photo-building" role="img" aria-label="Photo of the multi-storey office building exterior"></div>

    <div class="abs maroon" style="left:30px; top:221px; width:555px; height:14px;"></div>
    <div class="abs photo-gym" role="img" aria-label="Photo of the staff gym with equipment"></div>

    <div class="abs maroon" style="left:848px; top:406px; width:9px; height:139px;"></div>
    <div class="abs maroon" style="left:624px; top:535px; width:233px; height:10px;"></div>
    <div class="abs photo-boardroom" role="img" aria-label="Photo of the boardroom with meeting table"></div>

    <section class="abs facts">
      <div class="fact fact-name"><div class="fact-label">NAME:</div><div class="fact-value">Tavrinel House</div></div>
      <div class="fact"><div class="fact-label">ADDRESS:</div><div class="fact-value">27 Harlow Street Eastvale</div></div>
      <div class="fact"><div class="fact-label">WHEN DEVELOPED</div><div class="fact-value">2008</div></div>
      <div class="fact"><div class="fact-label">VALUE ON COMPLETION:</div><div class="fact-value">$87M</div></div>
      <div class="fact"><div class="fact-label">SIZE:</div><div class="fact-value">15,700M2 NLA</div></div>
      <div class="fact"><div class="fact-label">TYPE OF PROPERTY:</div><div class="fact-value">A Grade Commercial Office Space</div></div>
      <div class="fact"><div class="fact-label">QUALITY RATING:</div><div class="fact-value">4 STAR</div></div>
      <div class="fact fact-small"><div class="fact-label">DEVELOPED BY:</div><div class="fact-value">Arden Development Corporation Pty Ltd</div></div>
    </section>

    <section class="abs strategy">
      <h2 class="strategy-title">Development Strategy</h2>
      <div class="strategy-body">
        <p style="text-align:left;">Tavrinel is a world class mining engineering firm.<br>They had 6 offices spread out of a number of locations in the Southern part of Brisbane.</p>
        <p class="gap">Working with Tavrinel, we identified a site for their new headquarters. We purchased the land and applied for a development approval to develop a 15,700m2 office building on the site. We designed an office building around their requirements including their staff require&shy;ments, gym, bike rack, change rooms, outdoor dining areas, café, large car parking facility, storage etc.</p>
        <p>We appointed Corrigan Builders to undertake a “design and construct” contract to build the develop&shy;ment. Construction lasted about 18 months and we completed an integrated fitout to get them into the office space quicker.</p>
        <p style="text-align:left;">The property was sold on completion to American based fund manager Valmont for $87.2m</p>
      </div>
    </section>

    <div class="abs cta-button"><span>LOREM IPSUM IS SIMPLY DUMMY TEXT</span></div>

    <div class="abs call-title">CAll US AT</div>
    <div class="abs call-phone">your ph no goes here</div>

    <div class="abs rule-navy"></div>
    <svg class="abs web-band" viewBox="0 0 446 52" aria-hidden="true">
      <polygon points="18,0 446,0 446,52 0,52" fill="var(--maroon)"/>
    </svg>
    <div class="abs web-line">
      <svg width="18" height="18" viewBox="0 0 20 20" aria-hidden="true">
        <circle cx="10" cy="10" r="8.5" fill="none" stroke="#fff" stroke-width="1.8"/>
        <ellipse cx="10" cy="10" rx="3.8" ry="8.5" fill="none" stroke="#fff" stroke-width="1.5"/>
        <line x1="1.5" y1="10" x2="18.5" y2="10" stroke="#fff" stroke-width="1.5"/>
      </svg>
      <span>your web address goes here</span>
    </div>
  </article>
</div>
</body>
</html>
```